Property Report

8 page document, similar theme to our website (www.harbourandvale.example) and previous brochure (provided). All content provided. We want a professional looking document. We need ASAP. Thanks!

Industry/Entity Type

Property

Font styles to use
Serif
Sans Serif

Colors
ffc214
ffcf3e
fee18a
fff3d1

Requirements
Must have
• Page 1: Cover
Page 2: Content
Page 3: About Us
Page 4: Site Description
Page 5: Scheme
Page 6: Analysis
Page 7: Conclusion
Page 8: Contact Details

```html
<!DOCTYPE html>
<html lang="en">
<head>
<meta charset="utf-8">
<title>Site Report – Harbour &amp; Vale Commercial</title>
<link rel="stylesheet" href="https://fonts.googleapis.com/css2?family=Montserrat:wght@400;500;600;700;800&family=Open+Sans:wght@400;600;700&display=swap">
<style>
:root{
  --orange:#f6a615;
  --ink:#1c1c1c;
  --dark:#231f1c;
  --grey-band:rgba(70,70,70,.82);
  --cell:#dcdcdc;
  --cell-alt:#ebebeb;
  --paper:#ffffff;
  --backdrop:#f1f1f1;
  --line:#222;
}
*{margin:0;padding:0;box-sizing:border-box}
html,body{width:1200px;height:2414px;overflow:hidden}
body{background:var(--backdrop);position:relative;font-family:"Open Sans",Arial,sans-serif;color:var(--ink)}
.page{position:absolute;width:521px;height:750px;background:var(--paper);overflow:hidden;box-shadow:0 1px 4px rgba(0,0,0,.18)}
.col-left{left:70px}.col-right{left:631px}
.row-1{top:67px}.row-2{top:837px}.row-3{top:1606px}
.abs{position:absolute}
.heading{font-family:"Montserrat",Arial,sans-serif;font-weight:700;color:var(--orange);line-height:1}
.subheading{font-family:"Montserrat",Arial,sans-serif;font-weight:400;letter-spacing:4px;font-size:16px;color:#333;line-height:1}
.frame{position:absolute;border:1.5px solid var(--line)}
.photo{position:absolute}

/* cover */
.cover-band{left:25px;top:0;width:211px;height:750px;background:var(--orange)}
.cover-photo{left:0;top:178px;width:521px;height:399px;background:linear-gradient(115deg,#555 0%,#8a8a8a 45%,#777 70%,#6a6a6a 100%)}
.cover-tint{left:0;top:178px;width:236px;height:399px;background:linear-gradient(120deg,rgba(190,120,10,.8),rgba(220,145,15,.72))}
.cover-title{right:49px;top:40px;font-size:44px;text-align:right}
.cover-sub{right:49px;top:98px;text-align:right}
.brand{left:280px;top:320px;width:190px;text-align:center;font-family:"Montserrat",Arial,sans-serif;font-weight:700;color:#fff;font-size:34px;line-height:1.05}
.client{left:25px;top:617px;width:211px;text-align:center;color:#fff;font-family:"Montserrat",Arial,sans-serif}
.client .behalf{font-size:15px;letter-spacing:3px;font-weight:400}
.client .name{font-size:14px;letter-spacing:3px;font-weight:700;line-height:20px;margin-top:4px}
.client .rule{width:164px;height:1.5px;background:#333;margin:8px auto 14px}
.client .addr{font-size:10px;letter-spacing:2px;font-weight:700;line-height:14px}

/* contents */
.toc-photo{left:0;top:0;width:521px;height:750px;background:linear-gradient(135deg,#fff 0%,#fff 28%,#bdbdbd 42%,#3a3a3a 60%,#e8e8e8 100%)}
.toc-top{left:0;top:0;width:260px;height:178px;background:linear-gradient(90deg,#fff 70%,rgba(255,255,255,0))}
.toc-band{left:0;top:178px;width:521px;height:399px;background:var(--grey-band)}
.toc-title{left:44px;top:45px;font-size:36px}
.toc-sub{left:46px;top:98px}
.toc-pg{left:51px;top:281px;color:#fff;font-family:"Montserrat",Arial,sans-serif;font-weight:700;font-size:12px;letter-spacing:3px}
.toc-list{left:51px;top:305px;width:460px;list-style:none}
.toc-list li{display:flex;align-items:center;height:21px;color:#fff;font-family:"Montserrat",Arial,sans-serif;font-size:13px}
.toc-list .num{width:24px}
.toc-list .rule{width:232px;height:1px;background:#fff;margin-right:22px}
.toc-list .label{letter-spacing:3px}

/* text panels */
.panel{position:absolute;background:var(--orange);width:261px;height:399px;top:177px}
.panel-text{position:absolute;color:#fff;font-family:"Montserrat",Arial,sans-serif;font-weight:700;font-size:8.5px;letter-spacing:1.8px;line-height:12px;text-align:justify}
.panel-text p+p{margin-top:5px}
.tower{top:0;width:261px;height:750px}

/* comparables */
.comp-title{right:36px;top:30px;font-size:28px}
.comp{position:absolute;left:0;width:521px;height:200px}
.comp-frame{position:absolute;left:0;top:-11px;width:486px;height:197px;border-top:1px solid #555;border-bottom:1px solid #555;border-right:1px solid #555}
.comp-head{position:absolute;left:0;top:0;width:250px;height:24px;background:var(--orange);font-family:"Montserrat",Arial,sans-serif;font-weight:700;font-size:11px;letter-spacing:2px;line-height:24px;padding-left:23px;color:var(--ink)}
.comp-photo{left:250px;top:0;width:259px;height:173px;background:linear-gradient(135deg,#eee,#555 50%,#ddd)}
.comp-table{position:absolute;left:23px;top:43px;width:207px;border-collapse:separate;border-spacing:0 2px}
.comp-table th{background:var(--dark);color:#fff;font-family:"Montserrat",Arial,sans-serif;font-size:10px;font-weight:700;text-align:left;width:61px;height:24px;padding-left:8px}
.comp-table td{background:var(--cell);font-size:7.5px;letter-spacing:1px;padding-left:12px;line-height:9px}
.comp-table tr:nth-child(even) td{background:var(--cell-alt)}

/* analysis */
.ana-title{left:38px;top:30px;font-size:28px}
.ana-sub{left:38px;top:68px;font-family:"Montserrat",Arial,sans-serif;font-weight:700;font-size:14px}
.ana-intro{left:38px;top:91px;width:450px;font-size:10.5px;line-height:14px;color:#333}
.val-table{position:absolute;left:33px;top:133px;width:452px;border-collapse:separate;border-spacing:2px 1px}
.val-table th{background:var(--dark);color:#fff;font-weight:400;font-size:8px;width:70px;height:33px}
.val-table td{background:var(--cell);font-size:8px;text-align:center;color:#333}
.val-table tr:nth-child(even) td{background:var(--cell-alt)}
.rule-line{position:absolute;height:2px;background:var(--line)}
.yard-photo{left:0;top:375px;width:521px;height:338px;background:linear-gradient(180deg,#6f86a6 0%,#7d93b0 55%,#b65a2c 75%,#8f3f1e 100%)}
</style>
</head>
<body>

<!-- Cover -->
<section class="page col-left row-1" aria-label="Cover">
  <div class="abs cover-band"></div>
  <div class="photo cover-photo" role="img" aria-label="Upward view of a modern office tower"></div>
  <div class="abs cover-tint"></div>
  <div class="frame" style="left:236px;top:151px;width:236px;height:453px;border-left:none"></div>
  <h1 class="abs heading cover-title">SITE</h1>
  <p class="abs subheading cover-sub">REPORT</p>
  <p class="abs brand">Harbour &amp; Vale<br><span style="font-size:20px">Commercial</span></p>
  <div class="abs client">
    <p class="behalf">On behalf of</p>
    <p class="name">ASHFORD LANE<br>GROUP LIMITED</p>
    <div class="rule"></div>
    <p class="addr">18 Elmstead Road,<br>Northfield KT9 2QP</p>
  </div>
</section>

<!-- Contents -->
<section class="page col-right row-1" aria-label="Contents">
  <div class="photo toc-photo" role="img" aria-label="Black and white steel and glass roof structure"></div>
  <div class="abs toc-top"></div>
  <div class="abs toc-band"></div>
  <h2 class="abs heading toc-title">CONTENT</h2>
  <p class="abs subheading toc-sub">TABLE</p>
  <p class="abs toc-pg">PG.</p>
  <ul class="abs toc-list">
    <li><span class="num">3</span><span class="rule"></span><span class="label">About Us</span></li>
    <li><span class="num">4</span><span class="rule"></span><span class="label">Site Description</span></li>
    <li><span class="num">5</span><span class="rule"></span><span class="label">Scheme</span></li>
    <li><span class="num">6</span><span class="rule"></span><span class="label">Case Studies</span></li>
    <li><span class="num">7</span><span class="rule"></span><span class="label">Analysis</span></li>
    <li><span class="num">8</span><span class="rule"></span><span class="label">Conclusion</span></li>
    <li><span class="num">9</span><span class="rule"></span><span class="label">Contact Details</span></li>
  </ul>
</section>

<!-- About us -->
<section class="page col-left row-2" aria-label="About us">
  <h2 class="abs heading" style="right:296px;top:49px;font-size:36px">ABOUT</h2>
  <p class="abs subheading" style="right:296px;top:98px">US</p>
  <div class="frame" style="left:25px;top:150px;width:236px;height:452px;border-right:none"></div>
  <div class="panel" style="left:0"></div>
  <div class="panel-text" style="left:38px;top:232px;width:198px">
    <p>Harbour &amp; Vale Commercial specialise in the acquisition and disposal of development, investment and commercial property in London and the Home Counties. Our consultants advise on a wide range of property types and use classes and are experts in identifying ways in which property owners can maximise value.</p>
    <p>Our considerable knowledge of the property market and creative approach to delivering maximum value, has enabled us to become one of the most active development and investment consultancies in London and the South East.</p>
  </div>
  <div class="photo tower" style="left:260px;background:linear-gradient(160deg,#d6d6d6 0%,#9fb0bf 45%,#6f7f8c 100%)" role="img" aria-label="Glass office facade reflecting the sky"></div>
</section>

<!-- Site description -->
<section class="page col-right row-2" aria-label="Site description">
  <div class="photo tower" style="left:0;background:linear-gradient(170deg,#d0d0d0 0%,#7d8388 50%,#2f3236 100%)" role="img" aria-label="Corner of a dark glass building"></div>
  <h2 class="abs heading" style="left:300px;top:49px;font-size:36px">SITE</h2>
  <p class="abs subheading" style="left:300px;top:98px">DESCRIPTION</p>
  <div class="frame" style="left:260px;top:150px;width:236px;height:452px;border-left:none"></div>
  <div class="panel" style="left:260px"></div>
  <div class="panel-text" style="left:287px;top:245px;width:198px">
    <p>Harbour and Vale Commercial have been asked by Daniel Ashford the representative for Ashford Lane Group Limited to advise on the best disposal method to maximise value for their property.</p>
    <p>The existing property measures approximately 9,655 square feet internally with parking spaces.</p>
    <p>The site was granted permitted development rights in 2016 to be converted into 11 flats and 11 parking spaces but this was no implemented.</p>
    <p>We understand that the vendors operate their business from the premises and the property has a designated use class of B1(a) Office/E Class.</p>
  </div>
</section>

<!-- Comparables -->
<section class="page col-left row-3" aria-label="Comparables">
  <h2 class="abs heading comp-title">COMPARABLES</h2>

  <div class="comp" style="top:93px">
    <div class="comp-frame"></div>
    <div class="comp-head">Kestrel Housing Group</div>
    <div class="photo comp-photo" role="img" aria-label="Steel lattice roof detail"></div>
    <table class="comp-table">
      <tr><th>LOCATION</th><td>Linden Court, Station<br>Road, Northfield KT9 1AB</td></tr>
      <tr><th>UNIT</th><td>37 residential Units</td></tr>
      <tr><th>PRICE</th><td>£4,486,970</td></tr>
      <tr><th>PER UNIT</th><td>£121,000</td></tr>
      <tr><th>DATE</th><td>August 2019</td></tr>
    </table>
  </div>

  <div class="comp" style="top:309px">
    <div class="comp-frame"></div>
    <div class="comp-head">Kestrel Housing Group</div>
    <div class="photo comp-photo" role="img" aria-label="Steel lattice roof detail"></div>
    <table class="comp-table">
      <tr><th>LOCATION</th><td>Linden Court, Station<br>Road, Northfield KT9 1AB</td></tr>
      <tr><th>UNIT</th><td>37 residential Units</td></tr>
      <tr><th>PRICE</th><td>£4,486,970</td></tr>
      <tr><th>PER UNIT</th><td>£121,000</td></tr>
      <tr><th>DATE</th><td>August 2019</td></tr>
    </table>
  </div>

  <div class="comp" style="top:528px">
    <div class="comp-frame"></div>
    <div class="comp-head">Kestrel Housing Group</div>
    <div class="photo comp-photo" role="img" aria-label="Steel lattice roof detail"></div>
    <table class="comp-table">
      <tr><th>LOCATION</th><td>Linden Court, Station<br>Road, Northfield KT9 1AB</td></tr>
      <tr><th>UNIT</th><td>37 residential Units</td></tr>
      <tr><th>PRICE</th><td>£4,486,970</td></tr>
      <tr><th>PER UNIT</th><td>£121,000</td></tr>
      <tr><th>DATE</th><td>August 2019</td></tr>
    </table>
  </div>
</section>

<!-- Analysis -->
<section class="page col-right row-3" aria-label="Analysis">
  <h2 class="abs heading ana-title">ANALYSIS</h2>
  <p class="abs ana-sub">VALUATION</p>
  <p class="abs ana-intro">Lorem ipsum dolor sit amet, consectetur adipiscing elit. Curabitur consectetur elementum mauris sed consectetur. In hac habitasse platea dictumst.</p>
  <table class="val-table">
    <tr><th>£3,500,000</th><td>£4,100,000</td><td>£4,500,000</td><td>£4,900,000</td><td>£5,300,000</td><td>£5,700,000</td><td>£6,100,000</td></tr>
    <tr><th>£4,000,000</th><td>£3,600,000</td><td>£4,000,000</td><td>£4,400,000</td><td>£4,800,000</td><td>£5,200,000</td><td>£5,600,000</td></tr>
    <tr><th>£4,500,000</th><td>£3,100,000</td><td>£3,500,000</td><td>£3,900,000</td><td>£4,300,000</td><td>£4,700,000</td><td>£5,100,000</td></tr>
    <tr><th>£5,000,000</th><td>£2,600,000</td><td>£3,000,000</td><td>£3,400,000</td><td>£3,800,000</td><td>£4,200,000</td><td>£4,600,000</td></tr>
    <tr><th>£5,500,000</th><td>£2,100,000</td><td>£2,500,000</td><td>£2,900,000</td><td>£3,300,000</td><td>£3,700,000</td><td>£4,100,000</td></tr>
    <tr><th>£6,000,000</th><td>£1,600,000</td><td>£2,000,000</td><td>£2,400,000</td><td>£2,800,000</td><td>£3,200,000</td><td>£3,600,000</td></tr>
  </table>
  <div class="rule-line" style="left:0;top:360px;width:300px"></div>
  <div class="photo yard-photo" role="img" aria-label="Rear yard with blue cladding and timber decking"></div>
  <div class="rule-line" style="left:221px;top:724px;width:300px"></div>
</section>

</body>
</html>
```